Tea box package for Herbal Teas

We would like a design for a package of our tea products. We want the consumer to understand that our products are natural just by looking at the package. We prefer minimalistic designs.
The package we want would be a square (or slightly rectangular) box. The box would be generic enough for us to use it for different teas. Essentially what we want is all the main information and designs to be the same for each tea product we have. We would like to be able to change the main color and the name of the tea then to customize to the tea in the package. Please see the attached images for examples.
We really like the package in tea_packaging_example_4 picture. We would like our packaging to be something very similar but with all the labels printed on the package.
We already have our logo so I am attaching that as well (image named 'velk ansary logo copy'). That would go on the front of the box.
We also attach a tile created using our logo (see image called 'tile'). We would like this to go to the sides similarly to tea_packaging_example_4.
On the back of the pouch, we want to have directions on how to make the tea but we want this section to be editable. For now just 3-4 lines of sample text is fine along with instructions on how to make a tea, see picture 'back of tea box'.
We would like for the box color to be as in example picture
tea_packaging_example_4. The color of the writing should be the same as the logo color. The font style should be something that would look nice next to the logo font, we are not sure what that font should be. The only thing colored would be the name of the tea and the ribbon as seen in tea_packaging_example_4, which we would like to change if we need to, to other variations.
Thanks a lot. For any questions, please contact me.

```html
<!DOCTYPE html>
<html lang="en">
<head>
<meta charset="utf-8">
<title>Velk Ansary – Tropical Burst Tea Box</title>
<link rel="stylesheet" href="https://fonts.googleapis.com/css2?family=Tinos&family=Pathway+Gothic+One&family=Zilla+Slab:wght@300;400&display=swap">
<style>
  :root {
    --backdrop: #e7e3da;
    --kraft: #d7cdb3;
    --kraft-tile: #cfc4a8;
    --kraft-edge: #c9bd9f;
    --ribbon: #4b2b54;
    --ribbon-tile: #553460;
    --ribbon-deep: #3e2346;
    --base: #45284e;
    --base-tile: #3a2142;
    --gold: #dbd09d;
    --accent: #b43fc4;
    --ink: #1b1a18;
  }
  * { margin: 0; padding: 0; box-sizing: border-box; }
  html, body {
    width: 1200px;
    height: 1141px;
    overflow: hidden;
    background: var(--backdrop);
  }
  .canvas {
    position: relative;
    width: 1200px;
    height: 1141px;
  }
  .box-base {
    position: absolute;
    left: 120px;
    top: 910px;
    width: 960px;
    height: 179px;
    background: radial-gradient(ellipse at 50% 40%, var(--base-tile), var(--ribbon-deep) 60%, var(--base));
  }
  .lid {
    position: absolute;
    left: 100px;
    top: 52px;
    width: 1000px;
    height: 865px;
    background: var(--kraft);
    border: 1px solid var(--kraft-edge);
    text-align: center;
  }
  .lid-tile {
    position: absolute;
    inset: 0;
    background:
      radial-gradient(ellipse at 20% 20%, var(--kraft-tile), transparent 45%),
      radial-gradient(ellipse at 85% 15%, var(--kraft-tile), transparent 40%),
      radial-gradient(ellipse at 30% 95%, var(--kraft-tile), transparent 35%);
  }
  .brand-mark {
    position: absolute;
    left: 50%;
    top: 48px;
    width: 170px;
    height: 170px;
    margin-left: -85px;
    border: 3px solid var(--ink);
    border-radius: 50%;
  }
  .brand-name {
    position: absolute;
    left: 0;
    right: 0;
    top: 232px;
    font-family: "Tinos", serif;
    font-size: 40px;
    color: var(--ink);
    letter-spacing: 0.5px;
  }
  .ribbon {
    position: absolute;
    left: 0;
    right: 0;
    top: 317px;
    height: 459px;
    background: var(--ribbon);
    color: var(--gold);
  }
  .ribbon-tile {
    position: absolute;
    inset: 0;
    background:
      radial-gradient(ellipse at 22% 60%, var(--ribbon-tile), transparent 35%),
      radial-gradient(ellipse at 80% 35%, var(--ribbon-tile), transparent 38%);
  }
  .ribbon > p, .ribbon > h1, .ribbon > h2 { position: absolute; left: 0; right: 0; }
  .tea-name {
    top: 48px;
    font-family: "Tinos", serif;
    font-weight: 400;
    font-size: 68px;
    line-height: 1;
  }
  .tea-type {
    top: 138px;
    font-family: "Tinos", serif;
    font-weight: 400;
    font-size: 40px;
    line-height: 51px;
    text-transform: uppercase;
  }
  .ingredients {
    top: 248px;
    font-family: "Pathway Gothic One", sans-serif;
    font-size: 31px;
    line-height: 35px;
  }
  .blend-number {
    top: 330px;
    font-family: "Zilla Slab", serif;
    font-weight: 300;
    font-size: 34px;
    color: var(--accent);
  }
  .net-weight {
    top: 375px;
    font-family: "Tinos", serif;
    font-size: 28px;
  }
  .sachet-count {
    top: 416px;
    font-family: "Zilla Slab", serif;
    font-weight: 300;
    font-size: 25px;
  }
</style>
</head>
<body>
  <main class="canvas">
    <div class="box-base" role="img" aria-label="Purple box base with repeating brand tile pattern"></div>
    <section class="lid">
      <div class="lid-tile" role="img" aria-label="Faint tone-on-tone brand tile pattern on kraft lid"></div>
      <span class="brand-mark" aria-hidden="true"></span>
      <p class="brand-name">VELK ANSARY</p>
      <div class="ribbon">
        <div class="ribbon-tile" role="img" aria-label="Faint brand tile pattern on purple ribbon"></div>
        <h1 class="tea-name">Tropical Burst</h1>
        <h2 class="tea-type">Fruit tea with mango<br>and acai berries</h2>
        <p class="ingredients">Ingredients: Apple bits, hibiscus, mango, papaya, rosehip, beetroot, fig,<br>acai bits, maltodextrin, rice flour, citric acid and natural flavours.</p>
        <p class="blend-number">№0114</p>
        <p class="net-weight">Net Wt. 37.5g 1.3oz</p>
        <p class="sachet-count">Contains 15 individual tea sachets</p>
      </div>
    </section>
  </main>
</body>
</html>
```